High-end construction company needs a business card design

We need a modern looking business card that draws people in, is memorable and looks so good people will want to sick it on their fridges.
On the first side what is needed are:
Logo
My name - Tomas Verbelk
Title - Managing Director
Website - www.kravel.co.uk
Email - tomas@kravel.co.uk
Telephone - 020 5194 6381
Mobile - 07845319027
On the back side was is needed is a list of all the services we provide:
-Kitchen Renovations
-Bathroom Renovations
-House Renovations
-Garage Conversions
-Extensions
-Loft Conversions
-Conservatories
-Carpentry
-Tiling
-Electrical
-Plumbing & Heating
-Bricklaying
-Landscaping
-Decorating
-Plastering
We would like the colours to be the same shades as on the logo with grey or black for the words.
Target Market(s)
Anyone who needs building work done
Contact Information for Business Card
This business card is for a construction company which strives to deliver excellent service and quality.
The look and feel of the card should represent this.
Requirements
Must have
- On the first side what is needed are:
Logo
My name - Tomas Verbelk
Title - Managing Director
Website - www.kravel.co.uk
Email - tomas@kravel.co.uk
Telephone - 020 5194 6381
Mobile - 07845319027
Nice to have
- Cool looking features

```html
<!DOCTYPE html>
<html lang="en">
<head>
<meta charset="utf-8">
<title>Kravel Construction – Business Card</title>
<link href="https://fonts.googleapis.com/css2?family=Roboto:wght@400;500;700&family=Roboto+Condensed:wght@500;700&display=swap" rel="stylesheet">
<style>
  :root {
    --page-bg: #d6d6d6;
    --card-bg: #f1f1ef;
    --green-dark: #3f8a2b;
    --green-mid: #4f9a32;
    --green-light: #74b843;
    --ink: #1d1d1d;
    --ink-soft: #2e2e2e;
    --ghost: #c9c9c7;
  }
  * { box-sizing: border-box; margin: 0; padding: 0; }
  html, body { width: 1200px; height: 683px; overflow: hidden; }
  body {
    background: var(--page-bg);
    position: relative;
    font-family: "Roboto", Arial, sans-serif;
  }
  .card {
    position: absolute;
    width: 550px;
    height: 312px;
    background: var(--card-bg);
    border-radius: 0 28px 0 28px;
    overflow: hidden;
    box-shadow: 0 6px 16px rgba(0,0,0,0.18);
  }
  .card--front { left: 252px; top: 33px; z-index: 2; }
  .card--back { left: 489px; top: 343px; z-index: 1; }

  .wave { position: absolute; left: 0; top: 0; width: 550px; height: 312px; }

  /* Front */
  .brand {
    position: absolute;
    left: 42px;
    top: 118px;
    display: flex;
    align-items: center;
    gap: 10px;
    color: var(--green-mid);
    font-family: "Roboto Condensed", Arial, sans-serif;
    font-weight: 700;
  }
  .brand__mark { width: 14px; height: 14px; background: var(--green-mid); }
  .brand__name { font-size: 44px; line-height: 1; letter-spacing: 1px; }
  .brand__sub {
    position: absolute;
    left: 42px;
    top: 168px;
    color: var(--green-mid);
    font-family: "Roboto Condensed", Arial, sans-serif;
    font-weight: 700;
    font-size: 11.5px;
    letter-spacing: 3.2px;
  }
  .divider {
    position: absolute;
    width: 1.5px;
    background: var(--green-mid);
  }
  .card--front .divider { left: 247px; top: 54px; height: 158px; }

  .person { position: absolute; left: 295px; top: 30px; color: var(--green-mid); font-family: "Roboto Condensed", Arial, sans-serif; }
  .person__name { font-size: 19.5px; font-weight: 700; letter-spacing: 0.2px; }
  .person__title { font-size: 13.5px; font-weight: 700; margin-top: 6px; }

  .contact { position: absolute; left: 293px; display: flex; align-items: flex-start; gap: 11px; }
  .contact__icon { width: 30px; height: 30px; flex: none; }
  .contact__text { font-size: 17.5px; font-weight: 500; color: var(--ink); line-height: 23px; padding-top: 3px; }
  .contact--email { top: 98px; }
  .contact--phone { top: 143px; }
  .contact--web { top: 203px; }

  .tagline {
    position: absolute;
    left: 0; right: 0;
    top: 285px;
    text-align: center;
    color: #fff;
    font-family: "Roboto Condensed", Arial, sans-serif;
    font-weight: 500;
    font-size: 17px;
    letter-spacing: 0.2px;
  }

  /* Back */
  .site-scene {
    position: absolute;
    left: 4px; top: 20px;
    width: 300px; height: 230px;
    background: radial-gradient(ellipse at 40% 60%, var(--ghost) 0%, rgba(201,201,199,0.35) 55%, rgba(241,241,239,0) 75%);
    opacity: 0.7;
  }
  .services-heading {
    position: absolute;
    left: 87px; top: 25px;
    width: 376px; height: 34px;
    background: var(--green-mid);
    color: #eef5ea;
    font-family: "Roboto Condensed", Arial, sans-serif;
    font-weight: 500;
    font-size: 13.5px;
    line-height: 34px;
    text-align: center;
    letter-spacing: 0.2px;
  }
  .service-list {
    position: absolute;
    top: 92px;
    list-style: none;
    font-size: 14px;
    color: var(--ink-soft);
    line-height: 24.5px;
  }
  .service-list--one { left: 31px; }
  .service-list--two { left: 233px; }
  .service-list--three { left: 395px; }
  .card--back .divider { top: 101px; height: 93px; }
  .divider--first { left: 201px; }
  .divider--second { left: 365px; }

  .back-brand {
    position: absolute;
    left: 47px; top: 271px;
    color: #fff;
    font-family: "Roboto Condensed", Arial, sans-serif;
    font-weight: 700;
    line-height: 1;
  }
  .back-brand__name { font-size: 24px; letter-spacing: 1px; }
  .back-brand__sub { font-size: 6px; letter-spacing: 1.6px; margin-top: 3px; }
  .back-tagline {
    position: absolute;
    left: 208px; top: 282px;
    color: #fff;
    font-family: "Roboto Condensed", Arial, sans-serif;
    font-weight: 500;
    font-size: 12.5px;
    letter-spacing: 0.3px;
  }
</style>
</head>
<body>

<section class="card card--front" aria-label="Business card front">
  <svg class="wave" viewBox="0 0 550 312" aria-hidden="true">
    <path d="M290,262 C370,232 470,226 550,238 L550,312 L290,312 Z" fill="var(--green-light)"/>
    <path d="M0,262 C110,224 240,228 330,250 C420,272 495,274 550,264 L550,312 L0,312 Z" fill="var(--green-dark)"/>
  </svg>

  <div class="brand">
    <span class="brand__mark" aria-hidden="true"></span>
    <span class="brand__name">KRAVEL</span>
  </div>
  <div class="brand__sub">CONSTRUCTION LTD</div>

  <div class="divider"></div>

  <div class="person">
    <p class="person__name">TOMAS VERBELK,</p>
    <p class="person__title">MANAGING DIRECTOR</p>
  </div>

  <div class="contact contact--email">
    <svg class="contact__icon" viewBox="0 0 30 30" aria-hidden="true">
      <circle cx="15" cy="15" r="13.5" fill="none" stroke="var(--green-mid)" stroke-width="1.5"/>
      <rect x="9" y="11" width="12" height="8.5" rx="1" fill="var(--green-mid)"/>
      <path d="M9.5,11.5 L15,16 L20.5,11.5" fill="none" stroke="var(--card-bg)" stroke-width="1.2"/>
    </svg>
    <p class="contact__text">tomas@kravel.co.uk</p>
  </div>

  <div class="contact contact--phone">
    <svg class="contact__icon" viewBox="0 0 30 30" aria-hidden="true">
      <circle cx="15" cy="15" r="13.5" fill="none" stroke="var(--green-mid)" stroke-width="1.5"/>
      <path d="M11,9 L13.2,9 L14,12.2 L12.6,13.4 C13.4,15.3 14.7,16.6 16.6,17.4 L17.8,16 L21,16.8 L21,19 C21,20 20.2,20.6 19.2,20.5 C14.2,20 10,15.8 9.5,10.8 C9.4,9.8 10,9 11,9 Z" fill="var(--green-mid)"/>
    </svg>
    <p class="contact__text">020 5194 6381<br>07845319027</p>
  </div>

  <div class="contact contact--web">
    <svg class="contact__icon" viewBox="0 0 30 30" aria-hidden="true">
      <circle cx="15" cy="15" r="13.5" fill="none" stroke="var(--green-mid)" stroke-width="1.5"/>
      <circle cx="15" cy="15" r="7" fill="var(--green-mid)"/>
      <path d="M11,12 C13,11 14,13 13,15 C12,17 14,18 13,20 M17,9.5 C16,11 18,12 19.5,12.5" fill="none" stroke="var(--card-bg)" stroke-width="1.2"/>
    </svg>
    <p class="contact__text">www.kravel.co.uk</p>
  </div>

  <p class="tagline">WE DELIVER EXCELLENT SERVICE AND QUALITY</p>
</section>

<section class="card card--back" aria-label="Business card back">
  <div class="site-scene" role="img" aria-label="Faint grey silhouette of a site worker and tower cranes"></div>

  <p class="services-heading">KRAVEL CONSTRUCTION PROVIDES FOLLOWING SERVICES</p>

  <ul class="service-list service-list--one">
    <li>Kitchen Renovations</li>
    <li>Bathroom Renovations</li>
    <li>House Renovations</li>
    <li>Garage Conversions</li>
    <li>Extensions</li>
  </ul>
  <div class="divider divider--first"></div>
  <ul class="service-list service-list--two">
    <li>Loft Conversions</li>
    <li>Conservatories</li>
    <li>Carpentry</li>
    <li>Tiling</li>
    <li>Electrical</li>
  </ul>
  <div class="divider divider--second"></div>
  <ul class="service-list service-list--three">
    <li>Plumbing &amp; Heating</li>
    <li>Bricklaying</li>
    <li>Landscaping</li>
    <li>Decorating</li>
    <li>Plastering</li>
  </ul>

  <svg class="wave" viewBox="0 0 550 312" aria-hidden="true">
    <path d="M0,236 C90,218 190,226 290,252 C380,272 470,262 550,250 L550,312 L0,312 Z" fill="var(--green-light)"/>
    <path d="M0,256 C90,228 180,232 290,258 C380,276 470,268 550,256 L550,312 L0,312 Z" fill="var(--green-dark)"/>
  </svg>

  <div class="back-brand">
    <p class="back-brand__name">KRAVEL</p>
    <p class="back-brand__sub">CONSTRUCTION LTD</p>
  </div>
  <p class="back-tagline">IN DEPTH ESTIMATES AND WORK SCHEDULES.</p>
</section>

</body>
</html>
```